Business Card Design

Carl Brennow Insurance Agency, an Independent Insurance Agency which was stated on Pellham Row in Laplace, Louisiana on 1958 and has grown the six locations throughout South Louisiana. We sell personal (auto Homeowners flood, liability) and commercial insurance (commercial property, general liability, workers compensation, commercial auto). I am looking for a double sided card with list the five remaining locations on the back or maybe even a folded four sided card. Our home office is a two story building with a green roof. I have had a logo designed which I have attached. Open for revisions but would like to stay with in the same green roof over an M. I have attached the logo but can not tell if I was uploaded.

Target Market(s)

Individual and commercial insurance buyers. Upper income and business owners

Industry/Entity Type

Insurance

Requirements
Must have
• Must have similar logo as uploaded. Green roof over M or something similar. List all location address and phone numbers.

Employee name, office phone number; direct phone line; email address and website list all locations on card. Very Similar colors to current logo.
Nice to have
• Possible folded card with double sided print

```html
<!DOCTYPE html>
<html lang="en">
<head>
<meta charset="utf-8">
<title>Carl Brennow Insurance Agency – Business Card</title>
<link rel="stylesheet" href="https://fonts.googleapis.com/css2?family=Open+Sans:wght@400;600;700&family=Roboto:wght@700;900&display=swap">
<style>
  :root {
    --page-bg: #e9e6e1;
    --brand-blue: #1f6fc4;
    --brand-blue-dark: #2a5fae;
    --brand-green: #1f5a3a;
    --ink: #4a4a4a;
    --white: #ffffff;
    --card-shadow: 0 10px 28px rgba(0,0,0,0.22);
  }
  * { box-sizing: border-box; margin: 0; padding: 0; }
  html, body { width: 1200px; height: 900px; overflow: hidden; }
  body {
    background: var(--page-bg);
    font-family: "Open Sans", Arial, sans-serif;
    display: flex; flex-direction: column; align-items: center; justify-content: center;
    gap: 40px;
  }
  .card {
    width: 700px; height: 400px; position: relative; overflow: hidden;
    border-radius: 4px; box-shadow: var(--card-shadow);
  }

  /* Back side */
  .card-back { background: var(--brand-blue); color: var(--white); padding: 44px 50px; }
  .back-brand { display: flex; flex-direction: column; gap: 6px; }
  .brand-name {
    font-family: "Roboto", Arial, sans-serif; font-weight: 900;
    text-transform: uppercase; line-height: 1.05; letter-spacing: 0.5px;
  }
  .card-back .brand-name { font-size: 34px; color: var(--white); }
  .card-back .tagline { font-family: "Roboto", Arial, sans-serif; font-weight: 700; font-size: 18px; color: var(--white); }
  .locations {
    list-style: none; display: grid; grid-template-columns: repeat(3, 1fr);
    row-gap: 34px; column-gap: 20px; margin-top: 46px;
  }
  .location { display: flex; align-items: flex-start; gap: 10px; font-size: 16px; line-height: 1.35; }
  .pin { width: 16px; height: 22px; flex: none; margin-top: 3px; }

  /* Front side */
  .card-front { background: var(--white); }
  .front-brand { position: absolute; left: 52px; top: 140px; width: 300px; }
  .card-front .brand-name { font-size: 31px; color: var(--brand-green); }
  .card-front .tagline {
    font-family: "Roboto", Arial, sans-serif; font-weight: 700; font-size: 16px;
    color: var(--brand-green); margin-top: 6px;
  }
  .contact { position: absolute; left: 410px; top: 42px; color: var(--ink); }
  .person-name { font-family: "Roboto", Arial, sans-serif; font-weight: 700; font-size: 30px; color: var(--brand-green); line-height: 1; }
  .person-title { font-size: 15px; font-weight: 600; color: var(--ink); margin-top: 2px; }
  .address { font-size: 16px; line-height: 1.35; margin-top: 18px; }
  .contact-list { list-style: none; margin-top: 16px; font-size: 16px; line-height: 1.45; }
  .contact-list li { display: flex; align-items: center; gap: 8px; }
  .icon { width: 13px; height: 13px; flex: none; fill: var(--brand-green); }
  .front-wave { position: absolute; left: 0; bottom: 0; width: 700px; height: 150px; }
</style>
</head>
<body>

  <!-- Back side: locations -->
  <section class="card card-back" aria-label="Card back">
    <div class="back-brand">
      <div class="brand-name">Carl Brennow Insurance Agency</div>
      <div class="tagline">Serving Pellham Row Since 1958</div>
    </div>
    <ul class="locations">
      <li class="location"><svg class="pin" viewBox="0 0 16 22"><path d="M8 0a8 8 0 0 0-8 8c0 6 8 14 8 14s8-8 8-14a8 8 0 0 0-8-8z" fill="#1f5a3a"/><circle cx="8" cy="8" r="3" fill="#1f6fc4"/></svg><span>218 Bayou Court,<br>Laplace, LA 70068</span></li>
      <li class="location"><svg class="pin" viewBox="0 0 16 22"><path d="M8 0a8 8 0 0 0-8 8c0 6 8 14 8 14s8-8 8-14a8 8 0 0 0-8-8z" fill="#1f5a3a"/><circle cx="8" cy="8" r="3" fill="#1f6fc4"/></svg><span>218 Bayou Court,<br>Laplace, LA 70068</span></li>
      <li class="location"><svg class="pin" viewBox="0 0 16 22"><path d="M8 0a8 8 0 0 0-8 8c0 6 8 14 8 14s8-8 8-14a8 8 0 0 0-8-8z" fill="#1f5a3a"/><circle cx="8" cy="8" r="3" fill="#1f6fc4"/></svg><span>218 Bayou Court,<br>Laplace, LA 70068</span></li>
      <li class="location"><svg class="pin" viewBox="0 0 16 22"><path d="M8 0a8 8 0 0 0-8 8c0 6 8 14 8 14s8-8 8-14a8 8 0 0 0-8-8z" fill="#1f5a3a"/><circle cx="8" cy="8" r="3" fill="#1f6fc4"/></svg><span>218 Bayou Court,<br>Laplace, LA 70068</span></li>
      <li class="location"><svg class="pin" viewBox="0 0 16 22"><path d="M8 0a8 8 0 0 0-8 8c0 6 8 14 8 14s8-8 8-14a8 8 0 0 0-8-8z" fill="#1f5a3a"/><circle cx="8" cy="8" r="3" fill="#1f6fc4"/></svg><span>218 Bayou Court,<br>Laplace, LA 70068</span></li>
      <li class="location"><svg class="pin" viewBox="0 0 16 22"><path d="M8 0a8 8 0 0 0-8 8c0 6 8 14 8 14s8-8 8-14a8 8 0 0 0-8-8z" fill="#1f5a3a"/><circle cx="8" cy="8" r="3" fill="#1f6fc4"/></svg><span>218 Bayou Court,<br>Laplace, LA 70068</span></li>
    </ul>
  </section>

  <!-- Front side: contact -->
  <section class="card card-front" aria-label="Card front">
    <div class="front-brand">
      <div class="brand-name">Carl Brennow Insurance Agency</div>
      <div class="tagline">Serving Pellham Row Since 1958</div>
    </div>

    <div class="contact">
      <div class="person-name">Warren Hale</div>
      <div class="person-title">Managing Member</div>
      <p class="address">218 Bayou Court,<br>Laplace, LA 70068</p>
      <ul class="contact-list">
        <li><svg class="icon" viewBox="0 0 16 16"><path d="M3 1l3 3-2 2a10 10 0 0 0 6 6l2-2 3 3-2 2C7 15 1 9 1 3z"/></svg>(985) 555-0142</li>
        <li><svg class="icon" viewBox="0 0 16 16"><rect x="4" y="1" width="8" height="4"/><rect x="1" y="6" width="14" height="6" rx="1"/><rect x="4" y="10" width="8" height="5"/></svg>(985) 555-0143</li>
        <li><svg class="icon" viewBox="0 0 16 16"><path d="M4 0h8v16H4z M5 2v10h6V2z" fill-rule="evenodd"/></svg>(985) 555-0178</li>
        <li><svg class="icon" viewBox="0 0 16 16"><path d="M1 3h14v10H1z M2 4l6 5 6-5" fill-rule="evenodd"/></svg>warren@brennowins.com</li>
        <li><svg class="icon" viewBox="0 0 16 16"><circle cx="8" cy="8" r="7"/><path d="M1 8h14M8 1c-3 4-3 10 0 14M8 1c3 4 3 10 0 14" stroke="#fff" stroke-width="1" fill="none"/></svg>www.brennowins.com</li>
      </ul>
    </div>

    <svg class="front-wave" viewBox="0 0 700 150" preserveAspectRatio="none" aria-hidden="true">
      <path d="M0 40 C120 10 260 40 380 72 C500 100 600 95 700 78 L700 150 L0 150 Z" fill="#1f5a3a"/>
      <path d="M170 62 C300 60 400 95 520 102 C600 106 660 100 700 96 L700 116 C640 116 580 118 500 112 C380 104 290 72 170 62 Z" fill="#2a5fae"/>
      <path d="M170 62 C300 58 420 88 540 94 C610 97 660 92 700 86 L700 92 C650 98 600 100 520 98 C400 92 300 64 170 62 Z" fill="#ffffff"/>
    </svg>
  </section>

</body>
</html>
```